GIF Dynamic for Marketing Agency

Need a Dynamic GIF Created for Web Banner Placement. This is to Promote the Company, It's Products and Services on a Web Directory. Needs to contain a Creative Button/Call to Action such as 'Get Leads'

About the Company: Company is a Lead Generation Company Servicing Business Finance Professionals. Company Provides the Following Primary Products and Services:

-Lead Generation
-Live Calls
-Appointments
-Ads Management
-Aged Leads
-B2B Data
(2) Sizes: 250x250(Desktop) & 728 x 90 (Mobile)

*RECOMMENDED. Visit Company Website (See Logo) to Understand its Products & Services to develop insights as to what the company is looking for.

Target Market(s)

Business Loan Brokers

Industry/Entity Type

Marketing

Colors
0054AA
0677BA
7BADD7
CADEEF
E8F1F8
0094D4
00A9DD
6FCCEA
C7EBF8
E9F6FB
FFF300
FFF600
FEFA6F
FFFEC7
FFFEE8
EE7325
F08F49
F5BC92
FAE3D3
FDF4ED

Requirements
Must have
• Dynamic GIF. 2 Sizes. 250x250 & 728x90. CREATIVITY. Call to Action. Unique, Professional & Modern.
Nice to have
• Colorful
Should not have
• No Clipart Whatsoever.

```html
<!DOCTYPE html>
<html lang="en">
<head>
<meta charset="utf-8">
<title>Lead Generation Banner Set</title>
<link href="https://fonts.googleapis.com/css2?family=Poppins:wght@400;500;600;700;800&display=swap" rel="stylesheet">
<style>
  :root{
    --page:#f6f7fb;
    --ring:#eef0f7;
    --blue:#4b6ef0;
    --navy:#2f5eb5;
    --ink:#141821;
    --body:#4a4f5c;
    --white:#ffffff;
    --orange:#f07a22;
    --dot:#4b82f0;
    --skin:#c99575;
    --shirt:#4d6b9c;
  }
  *{box-sizing:border-box;margin:0;padding:0}
  html,body{width:1200px;height:900px;overflow:hidden}
  body{background:var(--page);font-family:"Poppins",sans-serif;position:relative}
  .bg-ring{position:absolute;border-radius:50%;border:70px solid var(--ring)}
  .bg-ring--top{width:520px;height:520px;left:850px;top:-160px}
  .bg-ring--bottom{width:360px;height:360px;left:-150px;top:750px;border-width:45px}

  .card{position:absolute;width:187px;height:187px;border-radius:6px;overflow:hidden;padding:8px 7px 0;box-shadow:0 8px 20px rgba(60,70,120,.08)}
  .card--tall{height:250px}
  .card--blue{background:var(--blue);color:var(--white)}
  .card--white{background:var(--white);color:var(--ink)}

  .brand{display:flex;align-items:center;gap:4px;font-size:6px;font-weight:700;height:9px;position:relative;z-index:2;white-space:nowrap}
  .brand-mark{width:10px;height:7px;background:currentColor;border-radius:1px;opacity:.85}
  .card--white .brand{color:var(--navy)}

  .headline{margin-top:12px;font-size:11.2px;line-height:16.5px;font-weight:800;letter-spacing:-.1px;white-space:nowrap;position:relative;z-index:2}
  .card--white .headline{color:var(--navy)}
  .sub{margin-top:9px;font-size:7.8px;line-height:10.5px;font-weight:600;text-transform:uppercase;white-space:nowrap;position:relative;z-index:2}

  .features{margin-top:6px;list-style:none;display:grid;grid-template-columns:90px 1fr;position:relative;z-index:2}
  .features--single{grid-template-columns:1fr;width:110px;margin-top:10px}
  .features--two{grid-auto-flow:column;grid-template-rows:repeat(3,16.5px)}
  .features li{height:16.5px;display:flex;align-items:center;gap:4px;font-size:7.6px;font-weight:400;white-space:nowrap}
  .card--white .features li{color:var(--body)}
  .features li::before{content:"";width:8px;height:8px;border-radius:50%;border:1.3px solid var(--white);background:radial-gradient(circle,var(--white) 0 2px,transparent 2.3px);flex:none}
  .card--white .features li::before{border-color:#bcd0f7;background:radial-gradient(circle,var(--dot) 0 2.4px,transparent 2.7px)}

  .cta{display:flex;align-items:center;justify-content:center;height:19px;margin-top:9px;background:var(--orange);color:var(--white);font-size:6px;font-weight:500;border-radius:4px;white-space:nowrap;box-shadow:0 4px 8px rgba(240,122,34,.3);position:relative;z-index:2}
  .cta--call{width:95px}
  .features--single + .cta{margin-top:10px}
  .cta--order{width:62px}

  .headline--photo{font-size:10.4px;line-height:12.5px;font-weight:700;margin-top:37px}
  .card--white .headline--photo{color:var(--ink)}

  .arrows{display:block;margin-top:4px;position:relative;z-index:2}

  .portrait{position:absolute;z-index:1;border-radius:48% 48% 0 0/30% 30% 0 0;background:linear-gradient(180deg,#3a2a22 0%,var(--skin) 18%,var(--skin) 34%,var(--shirt) 42%,#3e5b8b 100%)}
  .portrait--square{left:80px;top:22px;width:102px;height:165px}
  .portrait--tall{left:111px;top:109px;width:76px;height:141px}

  .ring{position:absolute;border-radius:50%;border:8px solid rgba(255,255,255,.08);z-index:0}
  .card--white .ring{border-color:#f2f4fa}
</style>
</head>
<body>
  <div class="bg-ring bg-ring--top"></div>
  <div class="bg-ring bg-ring--bottom"></div>

  <section class="card card--blue" style="left:381px;top:14px">
    <div class="brand"><span class="brand-mark"></span>LEADHARBOR.COM</div>
    <h2 class="headline">Increase Your Conversions<br>Get Access Today!</h2>
    <p class="sub">98% Active Line Status on All<br>Leads &amp; Data</p>
    <ul class="features features--two">
      <li>Lead Generation</li><li>Live Calls</li><li>Appointments</li>
      <li>Ads Management</li><li>Aged Leads</li><li>B2B Data</li>
    </ul>
    <span class="cta cta--call">Call Us 1-800-555-0142</span>
  </section>

  <section class="card card--blue" style="left:382px;top:215px">
    <div class="ring" style="left:-20px;top:140px;width:60px;height:60px"></div>
    <div class="brand"><span class="brand-mark"></span>LEADHARBOR.COM</div>
    <h2 class="headline headline--photo">Increase Your<br>Conversions<br>Get Access Today!</h2>
    <span class="cta cta--order">Order Online</span>
    <svg class="arrows" width="70" height="22" viewBox="0 0 70 22" fill="none" stroke="#ffffff" stroke-width="1.2" stroke-linecap="round">
      <path d="M2 20 C6 12 12 6 20 3"/><path d="M14 2 L20 3 L18 9"/>
      <path d="M60 20 C56 12 50 6 42 3"/><path d="M48 2 L42 3 L44 9"/>
    </svg>
    <div class="portrait portrait--square" role="img" aria-label="Smiling man in a blue t-shirt with arms crossed"></div>
  </section>

  <section class="card card--white card--tall" style="left:382px;top:417px">
    <div class="brand"><span class="brand-mark"></span>LEADHARBOR.COM</div>
    <h2 class="headline" style="margin-left:2px">Increase Your Conversions<br>Get Access Today!</h2>
    <p class="sub" style="margin-left:2px">98% Active Line Status on All<br>Leads &amp; Data</p>
    <ul class="features features--single" style="margin-left:2px">
      <li>Lead Generation</li><li>Live Calls</li><li>Appointments</li>
      <li>Ads Management</li><li>Aged Leads</li><li>B2B Data</li>
    </ul>
    <span class="cta cta--call" style="margin-left:2px">Call Us 1-800-555-0142</span>
    <div class="portrait portrait--tall" role="img" aria-label="Smiling man in a blue t-shirt with arms crossed"></div>
  </section>

  <section class="card card--white" style="left:382px;top:681px">
    <div class="ring" style="left:160px;top:120px;width:50px;height:50px"></div>
    <div class="brand"><span class="brand-mark"></span>LEADHARBOR.COM</div>
    <h2 class="headline">Increase Your Conversions<br>Get Access Today!</h2>
    <p class="sub">98% Active Line Status on All<br>Leads &amp; Data</p>
    <ul class="features features--two">
      <li>Lead Generation</li><li>Live Calls</li><li>Appointments</li>
      <li>Ads Management</li><li>Aged Leads</li><li>B2B Data</li>
    </ul>
    <span class="cta cta--call">Call Us 1-800-555-0142</span>
  </section>

  <section class="card card--white" style="left:608px;top:12px">
    <div class="ring" style="left:150px;top:-20px;width:50px;height:50px"></div>
    <div class="brand"><span class="brand-mark"></span>LEADHARBOR.COM</div>
    <h2 class="headline headline--photo">Increase Your<br>Conversions<br>Get Access Today!</h2>
    <span class="cta cta--order">Order Online</span>
    <svg class="arrows" width="70" height="22" viewBox="0 0 70 22" fill="none" stroke="#141821" stroke-width="1.2" stroke-linecap="round">
      <path d="M2 20 C6 12 12 6 20 3"/><path d="M14 2 L20 3 L18 9"/>
      <path d="M60 20 C56 12 50 6 42 3"/><path d="M48 2 L42 3 L44 9"/>
    </svg>
    <div class="portrait portrait--square" role="img" aria-label="Smiling man in a blue t-shirt with arms crossed"></div>
  </section>

  <section class="card card--blue card--tall" style="left:608px;top:214px">
    <div class="brand"><span class="brand-mark"></span>LEADHARBOR.COM</div>
    <h2 class="headline" style="margin-left:2px">Increase Your Conversions<br>Get Access Today!</h2>
    <p class="sub" style="margin-left:2px">98% Active Line Status on All<br>Leads &amp; Data</p>
    <ul class="features features--single" style="margin-left:2px">
      <li>Lead Generation</li><li>Live Calls</li><li>Appointments</li>
      <li>Ads Management</li><li>Aged Leads</li><li>B2B Data</li>
    </ul>
    <span class="cta cta--call" style="margin-left:2px">Call Us 1-800-555-0142</span>
    <div class="portrait portrait--tall" role="img" aria-label="Smiling man in a blue t-shirt with arms crossed"></div>
  </section>

  <section class="card card--white" style="left:608px;top:478px">
    <div class="ring" style="left:160px;top:125px;width:50px;height:50px"></div>
    <div class="brand"><span class="brand-mark"></span>LEADHARBOR.COM</div>
    <h2 class="headline">Increase Your Conversions<br>Get Access Today!</h2>
    <p class="sub">98% Active Line Status on All<br>Leads &amp; Data</p>
    <ul class="features features--two">
      <li>Lead Generation</li><li>Live Calls</li><li>Appointments</li>
      <li>Ads Management</li><li>Aged Leads</li><li>B2B Data</li>
    </ul>
    <span class="cta cta--call">Call Us 1-800-555-0142</span>
  </section>

  <section class="card card--blue" style="left:608px;top:680px">
    <div class="brand"><span class="brand-mark"></span>LEADHARBOR.COM</div>
    <h2 class="headline">Increase Your Conversions<br>Get Access Today!</h2>
    <p class="sub">98% Active Line Status on All<br>Leads &amp; Data</p>
    <ul class="features features--two">
      <li>Lead Generation</li><li>Live Calls</li><li>Appointments</li>
      <li>Ads Management</li><li>Aged Leads</li><li>B2B Data</li>
    </ul>
    <span class="cta cta--call">Call Us 1-800-555-0142</span>
  </section>
</body>
</html>
```